Creative Design "Size Chart" for a Clothing Product

Hi, My dear friends! I am looking to do a contest to design a unique creative "Size Chart" for our clothing line. See Attached the Sizes & Ideas Thanks Good Luck Dorian

Colors

Designer to choose colors to be used in the design.

```html
<!DOCTYPE html>
<html lang="en">
<head>
<meta charset="utf-8">
<title>Size Chart</title>
<link rel="stylesheet" href="https://fonts.googleapis.com/css2?family=Exo+2:wght@300;400&display=swap">
<style>
  :root {
    --ink: #5f5a59;
    --teal: #38a1bf;
    --pink: #c56198;
    --row-shade: #e6e6e6;
    --divider: #9a9a9a;
    --value: #555555;
    --guide-red: #e0262b;
    --paper: #ffffff;
  }
  html, body {
    margin: 0;
    padding: 0;
    width: 1200px;
    height: 1200px;
    overflow: hidden;
    background: var(--paper);
    font-family: "Exo 2", sans-serif;
  }
  .canvas {
    position: relative;
    width: 1200px;
    height: 1200px;
    overflow: hidden;
  }
  .sheet {
    position: absolute;
    left: -121.7px;
    top: -113.4px;
    width: 1932px;
    height: 1932px;
    transform: scale(0.74);
    transform-origin: 0 0;
  }
  .title-bar {
    position: absolute;
    left: 505px; top: 214px;
    width: 450px; height: 89px;
    background: var(--ink);
    color: #fff;
    font-size: 80px;
    font-weight: 300;
    line-height: 92px;
    padding-left: 14px;
    box-sizing: border-box;
    letter-spacing: 1px;
    white-space: nowrap;
  }
  .rule {
    position: absolute;
    left: 505px; width: 922px; height: 5px;
    background: var(--ink);
  }
  .size-table {
    position: absolute;
    left: 505px;
    --c: var(--teal);
  }
  .size-table.pink { --c: var(--pink); }
  .table-head {
    position: relative;
    height: 63px;
  }
  .group-name {
    position: absolute; left: 0; top: 0;
    width: 223px; height: 63px;
    background: var(--c);
    color: #fff;
    font-size: 46px;
    line-height: 66px;
    padding-left: 20px;
    box-sizing: border-box;
    white-space: nowrap;
  }
  .head-line {
    position: absolute; left: 223px; right: 0; bottom: 0;
    height: 6px; background: var(--c);
  }
  .size-tab {
    position: absolute; top: 0;
    width: 77px; height: 57px;
    background: var(--c);
    color: #fff;
    text-align: center;
    font-size: 30px;
    font-weight: 300;
    line-height: 57px;
  }
  .size-tab.with-num { line-height: 1; padding-top: 4px; box-sizing: border-box; }
  .size-tab small { display: block; font-size: 17px; margin-top: 2px; }
  .table-row {
    display: flex;
    height: 62px;
    align-items: stretch;
  }
  .table-row.shaded { background: var(--row-shade); }
  .row-label {
    width: 206px;
    padding-right: 32px;
    text-align: right;
    color: var(--c);
    font-size: 31px;
    line-height: 62px;
  }
  .cell {
    width: 97.7px;
    box-sizing: border-box;
    border-left: 3px solid var(--divider);
    text-align: center;
    color: var(--value);
    font-size: 26px;
    line-height: 62px;
    white-space: nowrap;
  }
  .section-bar {
    position: absolute;
    left: 800px; top: 1300px;
    width: 332px; height: 62px;
    background: var(--ink);
    color: #fff;
    text-align: center;
    font-size: 44px;
    font-weight: 300;
    line-height: 64px;
  }
  .figures {
    position: absolute;
    left: 485px; top: 1425px;
    width: 640px; height: 285px;
    background: linear-gradient(90deg, #e8e8e8, #f2f2f2);
  }
  .guide {
    position: absolute; left: 1188px;
    color: var(--ink);
  }
  .guide::before {
    content: ""; position: absolute; left: -16px; top: 0; bottom: 0;
    width: 2px; background: var(--guide-red);
  }
  .guide h3 { margin: 0; font-weight: 400; font-size: 30px; line-height: 32px; }
  .guide p { margin: 0; font-weight: 300; white-space: nowrap; }
  .guide-chest { top: 1425px; height: 136px; }
  .guide-chest p { font-size: 19px; line-height: 24px; }
  .guide-waist { top: 1635px; height: 75px; }
  .guide-waist p { font-size: 23px; line-height: 29px; }
</style>
</head>
<body>
<div class="canvas">
<div class="sheet">
  <div class="title-bar">Size Chart</div>
  <div class="rule" style="top:303px"></div>

  <div class="size-table" style="top:383px;width:827px">
    <div class="table-head">
      <div class="group-name">Mens</div><div class="head-line"></div>
      <div class="size-tab" style="left:250px">S</div>
      <div class="size-tab" style="left:348px">M</div>
      <div class="size-tab" style="left:446px">L</div>
      <div class="size-tab" style="left:543px">XL</div>
      <div class="size-tab" style="left:641px">2X</div>
      <div class="size-tab" style="left:739px">3X</div>
    </div>
    <div class="table-row"><div class="row-label">Chest</div><div class="cell">34-36</div><div class="cell">36-38</div><div class="cell">38-40</div><div class="cell">40-42</div><div class="cell">43-45</div><div class="cell">45-48</div></div>
    <div class="table-row shaded"><div class="row-label">Waist</div><div class="cell">28-30</div><div class="cell">30-32</div><div class="cell">32-34</div><div class="cell">34-36</div><div class="cell">36-40</div><div class="cell">40-44</div></div>
  </div>

  <div class="size-table pink" style="top:612px;width:922px">
    <div class="table-head">
      <div class="group-name">Womens</div><div class="head-line"></div>
      <div class="size-tab with-num" style="left:250px">XS<small>(0-2)</small></div>
      <div class="size-tab with-num" style="left:348px">S<small>(4-6)</small></div>
      <div class="size-tab with-num" style="left:446px">M<small>(8-10)</small></div>
      <div class="size-tab with-num" style="left:543px">L<small>(12-14)</small></div>
      <div class="size-tab with-num" style="left:641px">XL<small>(14-16)</small></div>
      <div class="size-tab with-num" style="left:739px">2X<small>(18)</small></div>
      <div class="size-tab with-num" style="left:836px">3X<small>(20)</small></div>
    </div>
    <div class="table-row"><div class="row-label">Chest</div><div class="cell">32-34</div><div class="cell">34-36</div><div class="cell">36-38</div><div class="cell">38-40</div><div class="cell">40-42</div><div class="cell">42-44</div><div class="cell">44-46</div></div>
    <div class="table-row shaded"><div class="row-label">Waist</div><div class="cell">26-28</div><div class="cell">28-30</div><div class="cell">30-32</div><div class="cell">32-34</div><div class="cell">34-36</div><div class="cell">36-38</div><div class="cell">38-40</div></div>
  </div>

  <div class="size-table" style="top:841px;width:827px">
    <div class="table-head">
      <div class="group-name">Boys</div><div class="head-line"></div>
      <div class="size-tab" style="left:250px">XXS</div>
      <div class="size-tab" style="left:348px">XS</div>
      <div class="size-tab" style="left:446px">S</div>
      <div class="size-tab" style="left:543px">M</div>
      <div class="size-tab" style="left:641px">L</div>
      <div class="size-tab" style="left:739px">XL</div>
    </div>
    <div class="table-row"><div class="row-label">Chest</div><div class="cell">20-23</div><div class="cell">23-26</div><div class="cell">26-29</div><div class="cell">29-32</div><div class="cell">32-35</div><div class="cell">35-38</div></div>
    <div class="table-row shaded"><div class="row-label">Waist</div><div class="cell">19-21</div><div class="cell">21-23</div><div class="cell">23-25</div><div class="cell">25-27</div><div class="cell">27-29</div><div class="cell">29-31</div></div>
  </div>

  <div class="size-table pink" style="top:1070px;width:827px">
    <div class="table-head">
      <div class="group-name">Girls</div><div class="head-line"></div>
      <div class="size-tab" style="left:250px">XXS</div>
      <div class="size-tab" style="left:348px">XS</div>
      <div class="size-tab" style="left:446px">S</div>
      <div class="size-tab" style="left:543px">M</div>
      <div class="size-tab" style="left:641px">L</div>
      <div class="size-tab" style="left:739px">XL</div>
    </div>
    <div class="table-row"><div class="row-label">Chest</div><div class="cell">19-22</div><div class="cell">22-25</div><div class="cell">25-28</div><div class="cell">28-31</div><div class="cell">31-34</div><div class="cell">34-37</div></div>
    <div class="table-row shaded"><div class="row-label">Waist</div><div class="cell">18-20</div><div class="cell">20-22</div><div class="cell">22-24</div><div class="cell">24-26</div><div class="cell">26-28</div><div class="cell">28-30</div></div>
  </div>

  <div class="rule" style="top:1360px"></div>
  <div class="section-bar">Measurement</div>

  <div class="figures" role="img" aria-label="Outline drawings of a man, woman, boy and girl with chest and waist measuring lines"></div>

  <div class="guide guide-chest">
    <h3>CHEST</h3>
    <p>Measure your chest around<br>the back and across your bust<br>for women/girl, or the largest<br>part of your chest for men/boy<br>going under your arms.</p>
  </div>
  <div class="guide guide-waist">
    <h3>WAIST</h3>
    <p>Measure around your<br>natural waistline.</p>
  </div>
</div>
</div>
</body>
</html>
```